Principle Minded Business and Life skills coach needs inspiring Wordpress design

I need a wordpress design for a new company I am starting called Rise4Bloom. I help ordinary people and entrepreneurs develop the skills, techniques and focus needed to succeed and lead a rewarding life. This site's objective is to promote my ability to help the visitor, give him quality info he can use now, and display subtle ads and offers that the visitor can purchase to help him implement what I am teaching him.

I am a devoted husband and loving father. I've owned several companies primarily in the technology and energy fields. I need a site that helps my clients feel connected with me and allows them to believe that I WILL help them achieve their goals.

I will be writing articles and blogs on this site as well as promoting products (third party products and ads to start, and my own later on).
Updates

Additional websites in market:http://www.pathguidehub.com/ Added Wednesday, January 21, 2015

Target Market(s)

starting entrepreneurs, struggling business people, people looking for personal growth, people looking for a home base business, network marketers.

Industry/Entity Type

Business

Requirements
Must have
• Blog
• Areas for adsense and other advertising
Nice to have
• My picture in the header
• Ability for my customers to book an appointment with me.
• Websites in similar market:
• http://brightstridecoach.com/
• http://tomvarkendalejournal.com/
• http://moneycompassguide.com/
• http://brennickgrowthtraining.com/

```html
<!DOCTYPE html>
<html lang="en">
<head>
<meta charset="utf-8">
<title>Rise4Bloom — Life &amp; Business Coaching</title>
<link href="https://fonts.googleapis.com/css2?family=Lato:wght@300;400;700;900&display=swap" rel="stylesheet">
<style>
:root{
  --blue:#3a95d8;
  --blue-dark:#2a7fc0;
  --orange:#f7941d;
  --green:#5cb85c;
  --ink:#2b3440;
  --text:#555d66;
  --muted:#9aa2aa;
  --soft:#f0f2f5;
  --line:#dfe3e8;
  --footer:#262a33;
  --white:#ffffff;
}
*{box-sizing:border-box;margin:0;padding:0}
html,body{width:856px;height:1200px;overflow:hidden}
body{position:relative;font-family:'Lato',sans-serif;color:var(--text);background:var(--white)}
.abs{position:absolute}

/* top bar */
.topbar{left:0;top:0;width:856px;height:24px;background:var(--blue);border-top:2px solid #6ec0f0}
.topbar .email{left:576px;top:8px;font-size:6.5px;color:var(--white)}
.topbar .social{top:7px;width:8px;height:8px;border-radius:50%;background:var(--white)}

/* header */
.header{left:0;top:24px;width:856px;height:45px;background:var(--white)}
.brand{left:167px;top:13px;font-size:16px;font-weight:400;color:var(--ink)}
.nav a{position:absolute;top:18px;font-size:8px;color:var(--muted);text-decoration:none}
.nav a.active{color:var(--blue)}

/* hero */
.hero{left:0;top:69px;width:856px;height:220px;overflow:hidden}
.hero-photo{left:0;top:0;width:470px;height:220px;background:linear-gradient(100deg,#4a5a2a 0%,#c88a3a 22%,#8a9a5a 45%,#a8c8e0 70%,#6a8a4a 100%)}
.hero-panel{left:0;top:0;width:856px;height:220px}
.hero h1{left:472px;top:58px;width:230px;font-size:19px;line-height:22.5px;font-weight:300;color:var(--white)}
.hero h1 b{font-weight:900}
.btn{display:block;background:var(--orange);color:var(--white);font-size:6.8px;font-weight:700;text-align:center;text-transform:uppercase}
.hero .btn{left:470px;top:158px;width:110px;height:22px;line-height:22px}

/* intro */
.intro{left:0;top:289px;width:856px;height:249px;background:var(--soft)}
.intro h2{left:168px;top:23px;font-size:13.5px;font-weight:700;color:var(--ink)}
.intro .portrait{left:167px;top:57px;width:75px;height:76px;background:linear-gradient(135deg,#6a4a32,#b88a62 55%,#e0c8a8)}
.intro .copy{left:256px;top:55px;width:253px;font-size:6.6px;line-height:10.7px;color:var(--text)}
.intro .copy p+p{margin-top:10.7px}
.ad-banner{left:172px;top:181px;width:325px;height:40px;background:linear-gradient(90deg,#dfe6ee 0%,#dfe6ee 37%,#1aa8c8 37%,#12a0c4 100%)}

.book h3{position:absolute;left:526px;top:21px;font-size:13px;font-weight:400;color:var(--blue)}
.field{position:absolute;left:525px;width:164px;background:var(--white);border:1px solid var(--line);font-size:5.8px;color:#aab0b6;padding:6px 8px}
.field.date{border-color:var(--blue);color:var(--ink);font-weight:700}
.field.date svg{position:absolute;right:5px;top:5px}
.submit{left:525px;top:200px;width:164px;height:20px;line-height:20px;background:var(--blue);color:var(--white);font-size:6.8px;font-weight:700;text-align:center;text-transform:uppercase}

/* lessons */
.lessons{left:0;top:538px;width:856px;height:214px;background:var(--white)}
.lessons h2{font-size:13.5px;font-weight:700;color:var(--ink);top:31px}
.lessons .rule{top:51px;width:75px;height:1.5px;background:var(--blue)}
.ticks{list-style:none;position:absolute;font-size:6.4px;line-height:10.7px;color:var(--text)}
.ticks li{position:absolute;left:0;padding-left:12px;width:100%}
.ticks li svg{position:absolute;left:0;top:3px}

/* events & video */
.media{left:0;top:752px;width:856px;height:238px;background:var(--soft)}
.media h2{top:22px;font-size:13.5px;font-weight:700;color:var(--ink)}
.media .divider{left:166px;top:43px;width:254px;height:1px;background:var(--line)}
.event{position:absolute;top:58px;width:120px}
.event .thumb{width:120px;height:93px}
.event h4{margin-top:13px;font-size:5.8px;letter-spacing:.8px;font-weight:900;color:var(--ink);text-transform:uppercase}
.event .meta{margin-top:4px;font-size:5.2px;letter-spacing:.6px;color:var(--text);text-transform:uppercase}
.event .excerpt{margin-top:5px;font-size:5.6px;line-height:10.5px;color:#b0b6bc}
.video{left:437px;top:58px;width:251px;height:147px;background:var(--white);padding:3px;box-shadow:0 1px 3px rgba(0,0,0,.35)}
.video .screen{position:relative;width:245px;height:141px;background:linear-gradient(110deg,#1e2a38 0%,#4a5a6a 45%,#9aa8b6 75%,#3a4858 100%)}
.video .controls{position:absolute;left:0;bottom:0;width:245px;height:16px;background:rgba(10,14,20,.8)}
.video .play{position:absolute;left:4px;top:2px;width:20px;height:12px;background:#222;border:1px solid #555}
.video .bar{position:absolute;left:35px;top:7px;width:180px;height:2px;background:#555}
.video .bar i{display:block;width:55px;height:2px;background:var(--blue)}

/* newsletter */
.newsletter{left:0;top:990px;width:856px;height:72px;background:var(--white)}
.newsletter .label{left:167px;top:32px;font-size:6px;letter-spacing:.8px;font-weight:900;color:var(--ink);text-transform:uppercase}
.newsletter .input{left:301px;top:25px;width:209px;height:22px;background:#eceff2;border:1px solid var(--line);font-size:6.4px;color:#7a828a;padding:7px 0 0 21px}
.newsletter .input svg{position:absolute;left:9px;top:8px}
.newsletter .subscribe{left:525px;top:25px;width:164px;height:22px;line-height:22px;background:var(--blue);color:var(--white);font-size:6.8px;font-weight:900;letter-spacing:.8px;text-align:center;text-transform:uppercase}

/* call to action */
.cta{left:0;top:1062px;width:856px;height:100px;background:var(--blue);text-align:center}
.cta p{position:absolute;left:0;top:20px;width:856px;font-size:12.5px;line-height:16px;font-weight:300;color:var(--white)}
.cta .btn{left:374px;top:63px;width:109px;height:21px;line-height:21px}

/* footer */
.footer{left:0;top:1162px;width:856px;height:38px;background:var(--footer);font-size:5.8px;color:#a8adb5}
.footer .copy{left:167px;top:16px}
.footer .copy span{color:var(--green)}
.footer .links a{position:absolute;top:16px;color:#a8adb5;text-decoration:none}
</style>
</head>
<body>

<div class="abs topbar">
  <span class="abs email">hello@rise4bloom.com</span>
  <span class="abs social" style="left:652px"></span>
  <span class="abs social" style="left:665px"></span>
  <span class="abs social" style="left:678px"></span>
</div>

<header class="abs header">
  <div class="abs brand">Rise4Bloom</div>
  <nav class="nav">
    <a class="active" style="left:502px">Home</a>
    <a style="left:552px">About</a>
    <a style="left:603px">Blog</a>
    <a style="left:648px">Contact</a>
  </nav>
</header>

<section class="abs hero">
  <div class="abs hero-photo" role="img" aria-label="Photo of the smiling coach outdoors in a blue shirt, with sunlit trees behind"></div>
  <svg class="abs hero-panel" width="856" height="220" viewBox="0 0 856 220">
    <polygon points="461,0 856,0 856,220 461,220 448,180 440,112" fill="#3a95d8"/>
  </svg>
  <h1 class="abs">Are you <b>ready</b> to take your life to a new level and <b>get the results</b> you truly desire?</h1>
  <a class="abs btn">Book appointment now</a>
</section>

<section class="abs intro">
  <h2 class="abs">Rise4Bloom will show you a new way of thinking</h2>
  <div class="abs portrait" role="img" aria-label="Portrait photo of the coach"></div>
  <div class="abs copy">
    <p>Whether you want to build a fulfilling career or business, achieve optimal health, create financial abundance, enjoy rewarding relationships, or take on any other goal in your life, Rise4Bloom will show you a new way of thinking and what to do to reach your dream.</p>
    <p>Leading by example, I’ll guide you through engaging, personalized and penetrating experiences and conversations and give you many practical tools to quickly set your life on a new and exciting trajectory. You will discover what you need to change in your life and how to make the change. You will develop new perspectives, clear decisions and a personal plan for making your decisions a</p>
  </div>
  <div class="abs ad-banner" role="img" aria-label="Advertising banner for a local car dealership offer"></div>

  <div class="book">
    <h3>Book an appointment today</h3>
    <div class="field" style="top:50px;height:17px;padding-top:5px">Name</div>
    <div class="field" style="top:73px;height:17px;padding-top:5px">Email</div>
    <div class="field date" style="top:98px;height:18px;padding-top:5px">15 January 2018
      <svg width="7" height="7" viewBox="0 0 7 7"><rect x="0.5" y="1" width="6" height="5.5" fill="none" stroke="#3a95d8"/><line x1="0.5" y1="2.5" x2="6.5" y2="2.5" stroke="#3a95d8"/></svg>
    </div>
    <div class="field" style="top:126px;height:68px">Message</div>
    <div class="abs submit">Submit now</div>
  </div>
</section>

<section class="abs lessons">
  <h2 class="abs" style="left:169px">You'll learn Life Design Basics</h2>
  <div class="abs rule" style="left:169px"></div>
  <ul class="ticks" style="left:169px;top:65px;width:250px">
    <li style="top:0"><svg width="6" height="5" viewBox="0 0 6 5"><path d="M0.5 2.5 L2.3 4.2 L5.5 0.8" fill="none" stroke="#3a95d8" stroke-width="1.2"/></svg>How to dream and uncover what you really want.</li>
    <li style="top:21px"><svg width="6" height="5" viewBox="0 0 6 5"><path d="M0.5 2.5 L2.3 4.2 L5.5 0.8" fill="none" stroke="#3a95d8" stroke-width="1.2"/></svg>How to be rid of self-sabotaging mental chatter and negative beliefs. “I am my own worst enemy” stops here!</li>
    <li style="top:53px"><svg width="6" height="5" viewBox="0 0 6 5"><path d="M0.5 2.5 L2.3 4.2 L5.5 0.8" fill="none" stroke="#3a95d8" stroke-width="1.2"/></svg>How to make and keep commitments to yourself around body, career, money, relationships, and more.</li>
    <li style="top:85px"><svg width="6" height="5" viewBox="0 0 6 5"><path d="M0.5 2.5 L2.3 4.2 L5.5 0.8" fill="none" stroke="#3a95d8" stroke-width="1.2"/></svg>How to have difficult conversations that will get you what you want.</li>
    <li style="top:106px"><svg width="6" height="5" viewBox="0 0 6 5"><path d="M0.5 2.5 L2.3 4.2 L5.5 0.8" fill="none" stroke="#3a95d8" stroke-width="1.2"/></svg>How to see yourself as a leader and creator in the world.</li>
  </ul>

  <h2 class="abs" style="left:435px">What to do to grow</h2>
  <div class="abs rule" style="left:435px;width:75px"></div>
  <ul class="ticks" style="left:435px;top:65px;width:260px">
    <li style="top:0"><svg width="6" height="5" viewBox="0 0 6 5"><path d="M0.5 2.5 L2.3 4.2 L5.5 0.8" fill="none" stroke="#3a95d8" stroke-width="1.2"/></svg>How to tell the truth in order to be proud and confident.</li>
    <li style="top:21px"><svg width="6" height="5" viewBox="0 0 6 5"><path d="M0.5 2.5 L2.3 4.2 L5.5 0.8" fill="none" stroke="#3a95d8" stroke-width="1.2"/></svg>How to gently shift your personality – and still be you.</li>
    <li style="top:43px"><svg width="6" height="5" viewBox="0 0 6 5"><path d="M0.5 2.5 L2.3 4.2 L5.5 0.8" fill="none" stroke="#3a95d8" stroke-width="1.2"/></svg>How to identify and understand your life lessons that keep repeating.</li>
    <li style="top:64px"><svg width="6" height="5" viewBox="0 0 6 5"><path d="M0.5 2.5 L2.3 4.2 L5.5 0.8" fill="none" stroke="#3a95d8" stroke-width="1.2"/></svg>How to design your life's mission</li>
  </ul>
</section>

<section class="abs media">
  <h2 class="abs" style="left:166px">Upcoming Events</h2>
  <div class="abs divider"></div>
  <article class="event" style="left:167px">
    <div class="thumb" role="img" aria-label="Photo of a joyful family jumping in a flower meadow under a blue sky" style="background:linear-gradient(180deg,#5a9ee0 0%,#cfe4f4 55%,#e8a040 80%,#5a8a3a 100%)"></div>
    <h4>This is your blog title here</h4>
    <div class="meta">27th July 2016 &nbsp;|&nbsp; Wordpress</div>
    <p class="excerpt">Lorem ipsum dolor sit amet, consectetur adipiscing elit. Duis ut lobortis nulla. Vestib-ulum ante ipsum primis in faucibus...</p>
  </article>
  <article class="event" style="left:301px">
    <div class="thumb" role="img" aria-label="Photo of a smiling group of friends together" style="background:linear-gradient(180deg,#f4f4f4 0%,#c8a890 50%,#8a6a58 100%)"></div>
    <h4>This is your blog title here</h4>
    <div class="meta">27th July 2016 &nbsp;|&nbsp; Wordpress</div>
    <p class="excerpt">Lorem ipsum dolor sit amet, consectetur adipiscing elit. Duis ut lobortis nulla. Vestib-ulum ante ipsum primis in faucibus...</p>
  </article>

  <h2 class="abs" style="left:437px">Watch Our Video</h2>
  <div class="abs video">
    <div class="screen" role="img" aria-label="Video still of two business people reviewing a tablet in an office">
      <div class="controls">
        <div class="play"><svg width="20" height="12" viewBox="0 0 20 12"><polygon points="8,3 8,9 13,6" fill="#fff"/></svg></div>
        <div class="bar"><i></i></div>
      </div>
    </div>
  </div>
</section>

<section class="abs newsletter">
  <div class="abs label">Subscribe to our newsletter</div>
  <div class="abs input">
    <svg width="8" height="6" viewBox="0 0 8 6"><rect x="0.5" y="0.5" width="7" height="5" fill="none" stroke="#9aa2aa" stroke-width="0.8"/><path d="M0.5 0.5 L4 3.2 L7.5 0.5" fill="none" stroke="#9aa2aa" stroke-width="0.8"/></svg>
    Enter your E-mail
  </div>
  <div class="abs subscribe">Subscribe</div>
</section>

<section class="abs cta">
  <p>If you are ready to do the work, I am ready to help you get<br>to the change you want in your life.</p>
  <a class="abs btn">Book appointment now</a>
</section>

<footer class="abs footer">
  <div class="abs copy">Copyright 2014 <span>Rise4Bloom</span> &nbsp;|&nbsp; All Rights Reserved</div>
  <nav class="links">
    <a style="left:632px">Privacy</a>
    <a style="left:665px">Sitemap</a>
  </nav>
</footer>

</body>
</html>
```